Update Business Card Design Project

We've been in business nearly 15 years and about 10 years ago developed a brand that is now well recognized. The business card is boring, too much print and nothing that says 'We are SIMPLY SPLENDID' right off the mark.
We are a fun store, lots of new things on a regular basis. Especially in kitchen goods where the colours are strong and the emphasis is on pretty and practical. We like to have both!
Updates
Hi there,
Target Market(s)
Store customers and suppliers
Demographics aged 40-70yrs, mid to high income, mostly women or couples, rural setting but in the 'shopping district' of our region. 1 hour to nearest city.
Industry/Entity Type
Business
Requirements
Nice to have
- Incorporate the logo, if possible

```html
<!DOCTYPE html>
<html lang="en">
<head>
<meta charset="utf-8">
<title>Simply Splendid – Business Card</title>
<link href="https://fonts.googleapis.com/css2?family=Arimo:wght@400;700&display=swap" rel="stylesheet">
<style>
  :root {
    --brown: #b0690f;
    --brown-dark: #9a5a0b;
    --gold: #f2c677;
    --gold-pale: #fbe6b5;
    --blush: #f3a489;
    --paper: #ffffff;
    --backdrop: #ecebe8;
  }
  * { box-sizing: border-box; margin: 0; padding: 0; }
  html, body {
    width: 1200px; height: 879px; overflow: hidden;
    background: var(--backdrop);
    font-family: "Arimo", Arial, sans-serif;
  }
  .sheet {
    position: relative; width: 1200px; height: 879px;
  }
  .card {
    position: absolute; left: 235px; width: 730px; height: 390px;
    border-radius: 22px; overflow: hidden; background: var(--paper);
    box-shadow: 0 6px 18px rgba(0,0,0,.18);
  }
  .card--front { top: 30px; }
  .card--back { top: 459px; }
  .card__art { position: absolute; inset: 0; width: 100%; height: 100%; }

  .brand {
    position: absolute; left: 160px; top: 130px;
    display: flex; align-items: center; gap: 26px;
    color: var(--brown);
  }
  .brand__mark {
    width: 92px; height: 92px; background: var(--brown);
  }
  .brand__name {
    font-weight: 700; text-transform: uppercase; line-height: 1;
  }
  .brand__title { font-size: 40px; letter-spacing: 3px; display: block; }
  .brand__tagline {
    display: block; margin-top: 10px; padding-top: 8px;
    border-top: 4px solid var(--brown);
    font-size: 17px; letter-spacing: 4px;
  }

  .contact {
    position: absolute; left: 0; right: 0; top: 106px;
    color: var(--brown); font-size: 21px; line-height: 27px;
    text-align: center; letter-spacing: .5px;
  }
  .contact__line { display: flex; justify-content: center; align-items: center; gap: 14px; }
  .contact__line--indent { padding-left: 40px; }
  .icon { width: 20px; height: 20px; flex: none; }
</style>
</head>
<body>
<main class="sheet">

  <section class="card card--front" aria-label="Card front">
    <svg class="card__art" viewBox="0 0 730 390" preserveAspectRatio="none" aria-hidden="true">
      <defs>
        <linearGradient id="frontSwoosh" x1="0" x2="1" y1="0" y2="0">
          <stop offset="0" stop-color="var(--gold)"/>
          <stop offset=".55" stop-color="var(--gold-pale)"/>
          <stop offset=".85" stop-color="var(--blush)"/>
          <stop offset="1" stop-color="#ffffff"/>
        </linearGradient>
      </defs>
      <path d="M0 0H730V46Q430 4 0 22Z" fill="var(--brown)"/>
      <path d="M0 230C180 300 430 335 730 318V390H0Z" fill="url(#frontSwoosh)"/>
      <path d="M0 272C230 345 480 360 730 302V390H0Z" fill="var(--brown)"/>
      <g fill="#ffffff" opacity=".13">
        <circle cx="95" cy="330" r="55"/>
        <circle cx="230" cy="370" r="34"/>
        <circle cx="605" cy="345" r="48"/>
        <circle cx="660" cy="18" r="30"/>
      </g>
    </svg>
    <div class="brand">
      <span class="brand__mark"></span>
      <span class="brand__name">
        <span class="brand__title">Simply Splendid</span>
        <span class="brand__tagline">Bed Bath &amp; Home</span>
      </span>
    </div>
  </section>

  <section class="card card--back" aria-label="Card back">
    <svg class="card__art" viewBox="0 0 730 390" preserveAspectRatio="none" aria-hidden="true">
      <defs>
        <linearGradient id="backSwoosh" x1="0" x2="1" y1="0" y2="0">
          <stop offset="0" stop-color="var(--gold)"/>
          <stop offset=".4" stop-color="var(--gold-pale)"/>
          <stop offset=".8" stop-color="var(--blush)"/>
          <stop offset="1" stop-color="#ffffff"/>
        </linearGradient>
      </defs>
      <path d="M0 0H730V22Q380 -8 0 14Z" fill="var(--brown)"/>
      <path d="M0 95C130 210 300 280 730 300V390H0Z" fill="url(#backSwoosh)"/>
      <path d="M0 290C220 335 470 340 730 318V390H0Z" fill="var(--brown)"/>
      <g fill="#ffffff" opacity=".14">
        <circle cx="95" cy="300" r="58"/>
        <circle cx="250" cy="345" r="40"/>
        <circle cx="590" cy="350" r="45"/>
      </g>
    </svg>
    <address class="contact">
      <p class="contact__line">
        <svg class="icon" viewBox="0 0 20 20" aria-hidden="true"><path d="M10 2 1 10h3v8h5v-5h2v5h5v-8h3Z" fill="none" stroke="var(--brown)" stroke-width="2"/></svg>
        <span>Harbour Point Plaza, 4150 Market Street</span>
      </p>
      <p class="contact__line contact__line--indent"><span>Elmridge, Nova Scotia, B0X 2K7</span></p>
      <p class="contact__line">
        <svg class="icon" viewBox="0 0 20 20" aria-hidden="true"><g fill="none" stroke="var(--brown)" stroke-width="1.8"><circle cx="10" cy="10" r="8"/><ellipse cx="10" cy="10" rx="3.5" ry="8"/><path d="M2 10h16"/></g></svg>
        <span>www.simplysplendidhome.ca</span>
      </p>
      <p class="contact__line">
        <svg class="icon" viewBox="0 0 20 20" aria-hidden="true"><circle cx="10" cy="10" r="8.5" fill="none" stroke="var(--brown)" stroke-width="1.8"/><path d="M7 5c-1 1-1 3 0 5s3 4 5 5c1 0 2-1 2-2l-2-1-1 1c-1-.5-2.5-2-3-3l1-1-1-2c-1 0-1 0-1-2Z" fill="var(--brown)"/></svg>
        <span>1 800 555 0142 . 902 555 0187</span>
      </p>
    </address>
  </section>

</main>
</body>
</html>
```